Blog Banner Design Project: Harbour Lantern Guides

Looking for a new banner for my blog " Owen Pelsworth's Harbour Lantern Guides" at http://www.harbourlanternguides-demo.net - and once design agreed also want an updated album art for the podcast that goes along with the site.
For more about the blog and what it is about:
http://www.harbourlanternguides-demo.net/about
Harbour Lantern Guides is a Luxury Travel Blog And Podcast that provides inspiration, advice and tips about luxurious travel experiences, including destinations, transportation, accommodation, and journeys, that travellers can read, listen to or watch.
Objective of the new design
(1) retain the colour scheme ideally to retain the brand identity, as have been using these colours since 2005.
(2) introduce more of my personality and make it more visually and overt that it is "Owen Pelsworth's Harbour Lantern Guides", so possibly introducing my image into the blog banner so visitors are clear and more aware of the person behind the brand.
(3) needs to have an up-market, luxury but modern feel.
(4) if possible reflect the focus on the content (destinations, transportation, accommodation, attractions and journeys) - but this maybe best left to just words as want the design to be bold and more of the branding and personality.
Ideal wording
Smallish: Owen Pelsworth's
Main wording: Harbour Lantern Guides
Sub-title/ small: luxurious destinations, transportation, accommodation and journeys.
I have a poll running with readers of my blog to rate the designs to help me to chose the final route, and so there is no need to submit any more designs. I will make the decision once the poll closes on the weekend.

```html
<!DOCTYPE html>
<html lang="en">
<head>
<meta charset="utf-8">
<title>Owen Pelsworth's Harbour Lantern Guides — Blog Banner</title>
<link rel="stylesheet" href="https://fonts.googleapis.com/css2?family=Anton&family=Arimo:ital,wght@1,400&display=swap">
<style>
  :root {
    --sky-top: #5e1f6e;
    --sky-mid: #a3307f;
    --sky-low: #d9486f;
    --horizon: #f59a3c;
    --sea-top: #e0608a;
    --sea-low: #9a3a8c;
    --silhouette: #1a0d1c;
    --title: #ece6ee;
    --kicker: #1e1420;
    --tagline: #f4eef6;
    --band: rgba(20, 6, 24, 0.45);
    --portrait-a: #2d2a4a;
    --portrait-b: #c59a86;
  }
  * { margin: 0; padding: 0; box-sizing: border-box; }
  html, body { width: 1200px; height: 172px; overflow: hidden; background: #fff; }

  .banner {
    position: relative;
    width: 1200px;
    height: 172px;
    overflow: hidden;
    background: linear-gradient(180deg,
      var(--sky-top) 0%,
      var(--sky-mid) 38%,
      var(--sky-low) 62%,
      var(--horizon) 73%,
      var(--sea-top) 80%,
      var(--sea-low) 100%);
  }

  .portrait {
    position: absolute;
    left: 0; top: 0;
    width: 212px; height: 172px;
    background: linear-gradient(165deg, var(--portrait-b) 0%, #9c6f6a 45%, var(--portrait-a) 100%);
  }

  .plane-art {
    position: absolute;
    left: 920px; top: 8px;
    width: 272px; height: 72px;
    background: linear-gradient(90deg, rgba(26,13,28,0.75), rgba(26,13,28,0.9));
    border-radius: 36px;
  }

  .palm-art {
    position: absolute;
    left: 990px; top: 86px;
    width: 210px; height: 86px;
    background: linear-gradient(180deg, rgba(26,13,28,0.55), rgba(26,13,28,0.9));
  }

  .tagline-band {
    position: absolute;
    left: 238px; top: 136px;
    width: 740px; height: 30px;
    background: linear-gradient(90deg, var(--band) 0%, var(--band) 80%, transparent 100%);
  }

  .kicker {
    position: absolute;
    left: 244px; top: 6px;
    font-family: "Anton", sans-serif;
    font-size: 26px;
    line-height: 1;
    letter-spacing: 0.5px;
    color: var(--kicker);
    white-space: nowrap;
  }

  .title {
    position: absolute;
    left: 242px; top: 42px;
    font-family: "Anton", sans-serif;
    font-weight: 400;
    font-size: 70px;
    line-height: 1.2;
    letter-spacing: 0.5px;
    color: var(--title);
    white-space: nowrap;
  }

  .tagline {
    position: absolute;
    left: 246px; top: 139px;
    font-family: "Arimo", sans-serif;
    font-style: italic;
    font-size: 20px;
    line-height: 1.2;
    color: var(--tagline);
    white-space: nowrap;
  }
</style>
</head>
<body>
  <header class="banner">
    <div class="portrait" role="img" aria-label="Portrait photo of the blog host, smiling"></div>
    <div class="plane-art" role="img" aria-label="Silhouette of a passenger aeroplane in flight"></div>
    <div class="palm-art" role="img" aria-label="Silhouettes of palm trees against the sunset"></div>
    <div class="tagline-band"></div>
    <p class="kicker">Owen Pelsworth's</p>
    <h1 class="title">Harbour Lantern Guides</h1>
    <p class="tagline">luxurious destinations, transportation, accommodation and journeys.</p>
  </header>
</body>
</html>
```